R T Security Flyer - Security Based Company

Security company offering installation of CCTV and Intruder alarm systems mainly but not limited to home alarms. Feel free to be creative

Target Market(s)

Residential and Commercial properties, Facility Managers, local business

Requirements
Must have
• smart professional finish, logo and latest up to date pictures if on kit

```html
<!DOCTYPE html>
<html lang="en">
<head>
<meta charset="utf-8">
<title>R T Security Flyer</title>
<link href="https://fonts.googleapis.com/css2?family=Exo+2:wght@400;500&family=Titillium+Web:wght@700&family=Oswald:wght@500&display=swap" rel="stylesheet">
<style>
:root{
  --peach:#fce3cd;
  --ink:#0b0b0b;
  --orange:#ee4e23;
  --white:#ffffff;
  --blue:#3a4fc0;
  --wall:#5b5b5e;
  --text-dark:#1a1a1a;
}
*{margin:0;padding:0;box-sizing:border-box}
html,body{width:1200px;height:848px;overflow:hidden;background:var(--peach)}
body{position:relative;font-family:"Exo 2",sans-serif}
.page{position:absolute;top:76px;width:493px;height:696px;background:var(--ink);overflow:hidden;box-shadow:6px 8px 10px rgba(0,0,0,.35)}
.page--front{left:80px}
.page--back{left:628px}
.page-label{position:absolute;top:798px;font-size:17px;color:var(--text-dark);font-family:"Exo 2",sans-serif}
.abs{position:absolute}

/* front */
.hero-photo{left:0;top:0;width:493px;height:332px;background:linear-gradient(160deg,#747477 0%,var(--wall) 50%,#3e3e41 100%)}
.hero-corner{left:0;top:0}
.brand{left:22px;top:104px;display:flex;align-items:center;gap:10px}
.brand__mark{width:14px;height:14px;background:var(--orange)}
.brand__name{font-family:"Exo 2",sans-serif;font-weight:500;font-size:19px;line-height:22px;color:var(--white)}
.headline{left:168px;top:168px;width:320px;text-align:center;font-family:"Titillium Web",sans-serif;font-weight:700;font-size:35px;line-height:40px;color:var(--white);text-shadow:1px 2px 3px rgba(0,0,0,.5)}
.headline em{font-style:normal;color:var(--orange)}
.features{left:10px;top:338px;width:370px;list-style:none}
.features li,.benefits li{position:relative;padding-left:14px;color:var(--white);font-size:10.2px;line-height:13px}
.features li::before,.benefits li::before{content:"";position:absolute;left:1px;top:4px;width:5px;height:5px;border:1.5px solid var(--orange);border-radius:50%}
.photo-keypad{left:382px;top:346px;width:98px;height:108px;transform:rotate(12deg);background:linear-gradient(135deg,#f4f4f6,#c9cbd1);border:3px solid var(--white)}
.photo-phones{left:378px;top:474px;width:98px;height:86px;transform:rotate(10deg);background:linear-gradient(135deg,#3c7fd6,#1d2f55 60%,#e8e8ea);border:3px solid var(--white)}
.footer-front{left:0;top:580px;width:493px;height:116px;background:var(--white)}
.cta{left:16px;top:8px;width:464px;height:40px;background:var(--orange);clip-path:polygon(0 0,100% 0,95% 100%,5% 100%);display:flex;align-items:center;justify-content:center;text-align:center;font-family:"Oswald",sans-serif;font-weight:500;font-size:12.4px;line-height:15.5px;color:var(--white)}
.badges{left:160px;top:52px;display:flex;align-items:center;gap:14px}
.badge-bar{width:86px;height:14px;background:#d8d8dc;border-radius:2px}
.badge-pill{width:56px;height:14px;background:#cfd8e6;border-radius:7px}
.badge-round{width:28px;height:28px;border:2px solid #3a3f70;border-radius:50%}
.contact{left:0;top:86px;width:493px;text-align:center;font-size:10.6px;line-height:13px;color:var(--text-dark)}

/* back */
.photo-siren{left:44px;top:44px;width:116px;height:144px;border-radius:18px;background:radial-gradient(circle at 50% 40%,#f3f3f3 0%,#d8d8d8 55%,#1f3a7a 90%,#0b0b0b 100%)}
.intro{left:217px;top:48px;width:258px;height:120px;border:1.5px solid var(--blue);padding:12px 8px 12px 14px;color:var(--orange);font-size:14.4px;line-height:18.4px;letter-spacing:.4px}
.benefits-tab{left:0;top:238px}
.benefits-title{left:16px;top:241px;color:var(--white);font-size:17.5px;letter-spacing:.3px;font-weight:400}
.benefits{left:9px;top:277px;width:470px;list-style:none}
.benefits li{font-size:12.2px;line-height:15px;padding-left:13px}
.benefits li::before{top:5px}
.benefits__more{display:block;max-width:442px;line-height:14.7px}
.photo-interior{left:0;top:572px;width:493px;height:124px;background:linear-gradient(90deg,#9fb2c4 0%,#d9d6cf 35%,#b4b0aa 60%,#e9e9eb 100%)}
.tagline{left:60px;top:580px;width:380px;height:44px;border-radius:22px;background:rgba(40,40,42,.8);display:flex;align-items:center;justify-content:center;text-align:center;font-family:"Oswald",sans-serif;font-weight:500;font-size:12.4px;line-height:15.5px;color:var(--white)}
</style>
</head>
<body>

<section class="page page--front">
  <div class="abs hero-photo" role="img" aria-label="Photo of two CCTV cameras mounted on a grey brick wall"></div>
  <svg class="abs hero-corner" width="210" height="210" viewBox="0 0 210 210"><path d="M0 0H200C200 120 130 200 0 205Z" fill="#0b0b0b"/></svg>
  <div class="abs brand">
    <span class="brand__mark"></span>
    <span class="brand__name">R T Security<br>Systems</span>
  </div>
  <h1 class="abs headline">Are you <em>looking to</em><br><em>keep you</em> or your<br>premises safe?</h1>

  <ul class="abs features">
    <li style="margin-bottom:11px">We Install, Maintain And Repair All<br>Intruder Alarms, Cctv, Intercom And Access Control</li>
    <li style="margin-bottom:7px">View, Control And Manage Your Security Systems<br>Anywhere In The World With Smartphone Apps</li>
    <li style="margin-bottom:14px">Feel At Ease With Monitoring Services And Police Response Tailored<br>To Suit You And Your Business</li>
    <li style="margin-bottom:26px">We Can Takeover Any Existing Security System And Offer Maintenance<br>Checks To Guarantee The Best Performance For You And Your Premises</li>
    <li style="margin-bottom:14px">we Understand That Being Security Conscious Is Ever Increasing, Pro-<br>tecting Your Property And Family Is A Number One Priority</li>
    <li>Our Fully Insured And Accredited Team Offer Quality,<br>Safety And Cost Efficiency Throughout And Whole Process</li>
  </ul>
  <div class="abs photo-keypad" role="img" aria-label="Photo of a finger pressing an alarm keypad"></div>
  <div class="abs photo-phones" role="img" aria-label="Photo of two smartphones showing a security app"></div>

  <div class="abs footer-front">
    <div class="abs cta">If you are looking to improve the security in your home, office or commercial<br>property then call a member of our team today for a free quote.</div>
    <div class="abs badges">
      <span class="badge-bar"></span>
      <span class="badge-pill"></span>
      <span class="badge-round"></span>
    </div>
    <p class="abs contact">operations@rtsecuritysystems.co.uk, www.rtsecuritysystems.co.uk,<br>14 Harlow Lane, Marden, Essex, CM9 2XT</p>
  </div>
</section>

<section class="page page--back">
  <div class="abs photo-siren" role="img" aria-label="Photo of an alarm siren box showing R T Security Systems and 01632 960 418"></div>
  <p class="abs intro">R T Security Systems are using<br>the latest cloud-based<br>technology to stay connected<br>with your home and business<br>24/7.</p>

  <svg class="abs benefits-tab" width="493" height="32" viewBox="0 0 493 32"><path d="M0 0H355L372 28H493V32H0Z" fill="#ee4e23"/></svg>
  <h2 class="abs benefits-title">Some benefits of cloud services are;</h2>

  <ul class="abs benefits">
    <li style="margin-bottom:7px">High level support 24/7</li>
    <li style="margin-bottom:10px">Reduce engineer call outs and running costs</li>
    <li style="margin-bottom:10px">Identify issues in advance</li>
    <li style="margin-bottom:7px">Remotely manage systems to ensure correct operation</li>
    <li style="margin-bottom:14px">Remote health checks carried out to keep<br>your system performing as it should</li>
    <li style="margin-bottom:12px">Automatically update your system with the latest releases via cloud<br>application software</li>
    <li>Interact, control and integrate your security system like never before
      <span class="benefits__more">With the new cloud-based system we can check the alarm performance anytime you need it. This gives us the capability to assist you in any of your needs, be that changing user codes or system configuration. We are always there, working in the background to make sure you have the support and help you need. This is taking alarm systems into the future and leaving the stand-alone systems in the past.</span></li>
  </ul>

  <div class="abs photo-interior" role="img" aria-label="Photos of a wall touch panel, a modern kitchen and an alarm keypad in a bright hallway"></div>
  <div class="abs tagline">R T Security Systems are always there,<br>always available, wherever and whenever you need us.</div>
</section>

<span class="page-label" style="left:298px">FRONT</span>
<span class="page-label" style="left:892px">BACK</span>

</body>
</html>
```